Loomvista: fashion design product software needs your help

Fashion design product software company requests your assistance in designing a complete stationary package around our new logo design. Our software assists fashion designers and apparel houses with efficient communication and streamlined production between each other and manufacturers throughout the entire project design life cycle.

The look should reflect clean, simple and modern design. Not too "techie." Must use the provided logo and colors (or variations on the chosen colors, i.e. percentages as needed).

Reference website: www.loomvista-example.com

Buzzwords: manufacturing, production, apparel design/ers, streamlined process, effective communication, business, production software.

Please try to tone down or make the colors more subtle with more simple design style, layout. No sewing  theme. Thank you.

Target Market(s)

fashion designers and apparel houses that use software to manage and track production process life cycle.

Industry/Entity Type

Communication

Requirements
Must have
• Use of the logo and colors-or variations of colors (attached)
Nice to have
• Playfulness but corporate: with a sense of practicality, economical, streamlined production. Embossing considered.
Should not have
• Please keep in mind economics both financially and economically. Save trees and money! We believe in tactile paper but not "fashion-y" or sparkly, over-the-top colors, effects or production.

```html
<!DOCTYPE html>
<html lang="en">
<head>
<meta charset="utf-8">
<title>Loomvista Stationery Set</title>
<link rel="stylesheet" href="https://fonts.googleapis.com/css2?family=Questrial&display=swap">
<style>
  :root {
    --board: #000000;
    --paper: #ffffff;
    --brand-brown: #6b3a26;
    --brand-blue: #2fa6dc;
    --panel-blue: #2aa3dd;
    --ink: #2b2b2b;
  }
  * { margin: 0; padding: 0; box-sizing: border-box; }
  html, body { width: 1200px; height: 831px; overflow: hidden; background: var(--board); }
  body { position: relative; font-family: "Questrial", "Century Gothic", sans-serif; color: var(--ink); }
  address { font-style: normal; }

  .brand-name { position: absolute; color: var(--brand-brown); font-weight: 400; line-height: 1; white-space: nowrap; }

  /* Letterhead */
  .letterhead { position: absolute; left: 28px; top: 28px; width: 563px; height: 753px; background: var(--paper); }
  .letterhead .brand-name { left: 268px; top: 108px; font-size: 44px; }
  .sender-block { position: absolute; left: 400px; top: 160px; font-size: 7px; line-height: 10px; color: var(--brand-brown); }
  .sender-block .label { color: var(--brand-blue); margin-right: 4px; }
  .recipient-block { position: absolute; left: 46px; top: 154px; font-size: 7.5px; line-height: 10.5px; }
  .letter-date { position: absolute; left: 46px; top: 282px; font-size: 7.5px; }
  .letter-body { position: absolute; left: 46px; top: 318px; width: 482px; font-size: 7.5px; line-height: 10.5px; }
  .letter-body p { margin-bottom: 10px; }
  .letter-body p.salutation { margin-bottom: 12px; }
  .closing { position: absolute; left: 46px; top: 700px; font-size: 7.5px; }
  .signature { position: absolute; left: 46px; top: 712px; width: 66px; height: 26px; }

  /* Blue panel */
  .panel { position: absolute; left: 594px; top: 28px; width: 578px; height: 753px; background: var(--panel-blue); }
  .panel .brand-name { left: 88px; top: 318px; font-size: 62px; color: #ffffff; opacity: 0.35; }

  /* Envelope */
  .envelope { position: absolute; left: 578px; top: 443px; width: 576px; height: 268px; background: var(--paper); box-shadow: 2px 3px 6px rgba(0,0,0,0.25); }
  .envelope .flap { position: absolute; left: 0; top: 0; }
  .envelope .brand-name { left: 0; width: 576px; text-align: center; top: 60px; font-size: 30px; }

  /* Business cards */
  .card { position: absolute; left: 310px; width: 282px; height: 150px; box-shadow: 2px 3px 6px rgba(0,0,0,0.3); }
  .card-front { top: 443px; background: var(--paper); }
  .card-front .brand-name { left: 22px; top: 34px; font-size: 30px; }
  .card-front .card-details { position: absolute; left: 66px; top: 80px; font-size: 6.5px; line-height: 9px; color: var(--brand-brown); }
  .card-front .label { color: var(--brand-blue); }
  .card-back { top: 596px; background: var(--brand-brown); }
  .card-back .card-details { position: absolute; left: 66px; top: 70px; font-size: 6.5px; line-height: 9px; color: var(--brand-blue); }
  .card-details .label { margin-right: 4px; }
</style>
</head>
<body>

<section class="letterhead">
  <p class="brand-name">Loomvista</p>

  <address class="recipient-block">
    Nora Pennell<br>14 Linden Row<br>Mill Street<br>Eastbrook<br>County EB4 2QP
  </address>

  <address class="sender-block">
    Loomvista Technologies Corp.<br>220 Mercer Plaza<br>New York, NY 10012<br><br>
    <span class="label">T</span>555-014-2290<br>
    <span class="label">E</span>contact@loomvista-example.com<br>
    www.loomvista-example.com
  </address>

  <p class="letter-date">18 September 2010</p>

  <div class="letter-body">
    <p class="salutation">Dear Ms Pennell</p>
    <p>Our team has reviewed your request and prepared a summary of the production schedule for the coming season. The attached notes cover sampling, fabric sourcing and factory approvals, along with the dates we discussed last week.</p>
    <p>Each stage of the project is now tracked in one shared workspace, so designers, pattern makers and suppliers see the same status at the same time.</p>
    <p>Approved tech packs are sent directly to the manufacturer, and any change requested by the factory returns to your desk for review before it is applied. This keeps revisions clear and avoids costly delays on the floor. Costing sheets, trim lists and size charts travel with each style, so nothing is lost between teams.</p>
    <p>We would also like to schedule a short training session for your production staff. The session covers reporting, order tracking and supplier messaging, and it can be held at your studio or online, whichever suits the team best. Each attendee will receive a short guide and access to our support desk for the first month.</p>
    <p>Our account managers will check in after the first delivery cycle to review results, gather feedback and suggest small adjustments to your workflow where they would save time or reduce cost.</p>
    <p>Please let us know which dates work for you, and we will send a confirmed agenda along with the updated license terms for the new season.</p>
    <p>Thank you again for choosing our platform. We look forward to working with you.</p>
  </div>

  <p class="closing">Kind regards</p>
  <svg class="signature" role="img" aria-label="Handwritten signature" viewBox="0 0 66 26">
    <rect x="0" y="4" width="66" height="18" rx="9" fill="#2fa6dc" opacity="0.35"/>
  </svg>
</section>

<section class="panel">
  <p class="brand-name">Loomvista</p>
</section>

<section class="envelope">
  <svg class="flap" width="576" height="268" viewBox="0 0 576 268">
    <polyline points="0,0 288,46 576,0" fill="none" stroke="#d2d2d2" stroke-width="1"/>
  </svg>
  <p class="brand-name">Loomvista</p>
</section>

<section class="card card-front">
  <p class="brand-name">Loomvista</p>
  <address class="card-details">
    Loomvista Technologies Corp.<br>220 Mercer Plaza<br>New York, NY 10012<br>
    <span class="label">T</span>555-014-2290<br>
    <span class="label">E</span>contact@loomvista-example.com<br>
    www.loomvista-example.com
  </address>
</section>

<section class="card card-back">
  <address class="card-details">
    Dana Whitlock<br>Director of Development<br>Loomvista Technologies Corp.<br><br>
    <span class="label">T</span>555-014-2290<br>
    <span class="label">E</span>contact@loomvista-example.com
  </address>
</section>

</body>
</html>
```